Rebranding of WordPress website | Velcor and Sons

We currently have a wordpress website www.brightkettlebrews.com.au that we need rebranded to Velcor and Sons and modernised. Velcor and Sons is an import export business. The website is also linked to Shopify.The current website was created as a coffee website but will now need to have the main page then have the 3 product pages of a menu. Our New web address is www.velcorandsons.com.au Our general Enquiries email is enquiries@velcorandsons.com.au and we are also on Facebook and Instagram. We are looking for a clean fresh looking website, not too fussy. Black, white, natural textures.

```html
<!DOCTYPE html>
<html lang="en">
<head>
<meta charset="utf-8">
<title>Velcor &amp; Sons</title>
<link href="https://fonts.googleapis.com/css2?family=Poppins:wght@400;500;600&display=swap" rel="stylesheet">
<style>
:root{
  --ink:#1e1916;
  --dark:#2b231e;
  --darker:#15110f;
  --tan:#b59c78;
  --tan-dark:#9c8462;
  --white:#ffffff;
  --paper:#f4f2ef;
  --muted:#cfc6bb;
  --grey:#7a7470;
}
*{margin:0;padding:0;box-sizing:border-box}
html,body{width:1200px;height:3208px;overflow:hidden}
body{font-family:"Poppins",sans-serif;color:var(--ink);background:var(--white);position:relative}
.abs{position:absolute}
.btn{position:absolute;background:var(--tan);color:var(--white);font-size:15px;border-radius:20px;display:flex;align-items:center;justify-content:center}

/* header */
.site-header{position:absolute;top:0;left:0;width:1200px;height:80px;background:var(--white);z-index:3}
.brand-box{position:absolute;left:192px;top:0;width:128px;height:152px;background:var(--white);z-index:4;display:flex;align-items:center;justify-content:center;box-shadow:0 4px 10px rgba(0,0,0,.25)}
.brand-box .mark{width:100px;height:100px;background:var(--ink);color:var(--white);font-weight:600;font-size:18px;line-height:1.1;display:flex;align-items:center;justify-content:center;text-align:center}
.nav{position:absolute;right:80px;top:44px;display:flex;gap:44px;font-size:14px}
.nav .active{border-bottom:2px solid var(--ink);padding-bottom:6px}

/* hero */
.hero{position:absolute;top:80px;left:0;width:1200px;height:600px;background:linear-gradient(100deg,#2b221d 0%,#3a2c23 45%,#20324a 70%,#2a1d15 100%)}
.hero h1{position:absolute;left:176px;top:300px;font-size:76px;font-weight:600;color:var(--white)}
.hero p{position:absolute;left:176px;top:410px;width:440px;font-size:13px;line-height:22px;color:var(--muted)}
.dots{position:absolute;left:578px;top:522px;display:flex;gap:8px}
.dots i{width:10px;height:10px;border-radius:50%;background:var(--white);opacity:.6}
.dots i:first-child{opacity:1}

/* about */
.about{position:absolute;top:680px;left:0;width:1200px;height:540px;background:var(--white)}
.about .photo{position:absolute;left:144px;top:100px;width:376px;height:340px;border-radius:14px;background:radial-gradient(circle at 50% 45%,#dfe6ee 0%,#5d7390 35%,#0e1622 75%)}
.about h2{position:absolute;left:552px;top:106px;font-size:42px;font-weight:600}
.about p{position:absolute;left:552px;top:180px;width:510px;font-size:13px;line-height:24px;color:var(--grey)}
.edge{position:absolute;left:0;width:1200px;height:30px}

/* products */
.products{position:absolute;top:1200px;left:0;width:1200px;height:760px;background:linear-gradient(160deg,#2e241e,#1c1612 60%,#2a201a)}
.section-title{position:absolute;left:0;width:1200px;display:flex;align-items:center;justify-content:center;gap:40px;color:var(--white);font-size:40px;font-weight:500}
.section-title span.rule{width:150px;height:2px;background:var(--muted)}
.card{position:absolute;top:186px;width:260px;height:380px;background:var(--white);text-align:center}
.card .pack{position:absolute;left:70px;top:22px;width:120px;height:180px;border-radius:6px;background:linear-gradient(180deg,#3a3a3a,#111 60%,#6b1a14)}
.card .pack.light{background:linear-gradient(180deg,#e9dcc0,#c4a86f)}
.card h3{position:absolute;top:222px;width:100%;font-size:24px;font-weight:600}
.card .wt{position:absolute;top:258px;width:100%;font-size:11px;color:var(--grey)}
.card .price{position:absolute;top:278px;width:100%;font-size:16px}
.card .btn{left:90px;top:322px;width:80px;height:26px;font-size:11px}

/* testimonials */
.testimonials{position:absolute;top:1960px;left:0;width:1200px;height:520px;background:linear-gradient(180deg,#3a302a,#5a4a3e 50%,#2a221d)}
.quote-box{position:absolute;left:200px;top:160px;width:800px;height:328px;border:4px solid var(--tan);background:rgba(25,20,17,.55);text-align:center;color:var(--white)}
.quote-box h4{margin-top:48px;font-size:24px;font-weight:500}
.quote-box .role{font-size:12px;color:var(--muted);margin-top:4px}
.quote-box p{width:620px;margin:30px auto 0;font-size:12px;line-height:24px;color:var(--muted)}
.arrow{position:absolute;top:320px;width:40px;height:40px;border-radius:50%;background:var(--white);display:flex;align-items:center;justify-content:center}

/* partners */
.partners{position:absolute;top:2480px;left:0;width:1200px;height:130px;background:var(--paper);display:flex;justify-content:center;align-items:center;gap:52px}
.partners i{width:120px;height:40px;border-radius:20px;background:#cfcac5}

/* footer */
.footer{position:absolute;top:2600px;left:0;width:1200px;height:568px;background:linear-gradient(180deg,#2b231e,#1a1411)}
.vip{position:absolute;left:140px;top:20px;width:920px;height:84px;background:var(--darker);border-radius:16px}
.vip h3{position:absolute;left:48px;top:18px;font-size:26px;font-weight:500;color:var(--white)}
.vip .field{position:absolute;left:392px;top:24px;width:276px;height:36px;border-radius:18px;background:var(--white);font-size:12px;color:#999;padding:9px 18px}
.vip .btn{left:686px;top:24px;width:120px;height:36px;border-radius:18px;font-size:14px}
.social{position:absolute;top:24px;width:36px;height:36px;border-radius:50%;background:var(--white)}
.foot-brand{position:absolute;left:184px;top:200px;width:128px;height:120px;background:var(--white);display:flex;align-items:center;justify-content:center}
.foot-brand .mark{width:104px;height:96px;background:var(--ink);color:var(--white);font-weight:600;font-size:18px;line-height:1.1;display:flex;align-items:center;justify-content:center;text-align:center}
.foot-text{position:absolute;left:184px;top:374px;width:300px;font-size:12px;line-height:22px;color:var(--muted)}
.col-title{position:absolute;top:158px;font-size:24px;font-weight:500;color:var(--white)}
.col-title::after{content:"";display:block;width:140px;height:1px;background:var(--grey);margin-top:10px}
.links{position:absolute;left:586px;top:224px;list-style:none;font-size:12px;line-height:32px;color:var(--muted)}
.contact{position:absolute;left:784px;font-size:12px;color:var(--muted);display:flex;gap:14px;align-items:flex-start;line-height:22px}
.contact svg{flex:none;margin-top:2px}
.bottom-bar{position:absolute;top:3168px;left:0;width:1200px;height:40px;background:#0f0c0a;font-size:11px;color:var(--grey);display:flex;justify-content:space-between;align-items:center;padding:0 150px}
</style>
</head>
<body>

<header class="site-header">
  <nav class="nav">
    <span class="active">Home</span><span>Products</span><span>Chamber We Support</span><span>VIP Club</span><span>Contact Us</span>
  </nav>
</header>
<div class="brand-box"><div class="mark">VELCOR<br>&amp; SONS</div></div>

<section class="hero" role="img" aria-label="Photo of a cup of black coffee beside a wooden scoop of roasted coffee beans on a dark table">
  <h1>Velcor &amp; Sons</h1>
  <p>Fine beans sourced from trusted growers and roasted with care. We import and export quality coffee so every cup you pour is rich, smooth and full of honest flavour.</p>
  <div class="btn" style="left:176px;top:490px;width:100px;height:30px;font-size:12px">Read More</div>
  <div class="dots"><i></i><i></i><i></i></div>
</section>

<section class="about">
  <svg class="edge" style="top:-14px" viewBox="0 0 1200 30" preserveAspectRatio="none"><path d="M0 14 L60 8 L140 18 L230 6 L330 16 L420 9 L520 19 L610 7 L720 17 L820 8 L910 18 L1010 6 L1110 16 L1200 9 L1200 30 L0 30Z" fill="#fff"/></svg>
  <div class="photo" role="img" aria-label="Photo of hands holding a glowing globe of the world"></div>
  <h2>About Velcor &amp; Sons</h2>
  <p>Velcor and Sons is a family import and export business bringing quality goods from trusted partners around the world to kitchens and cafes across the country. What began as a small coffee venture has grown into a wider trade house with a simple promise: source well, deal fairly and deliver on time. We work closely with growers and makers, check every shipment with care and keep our range lean so that each product earns its place on the shelf. Our team blends years of trade know-how with a love of good food and drink, and we are proud to share it with you.</p>
  <div class="btn" style="left:552px;top:408px;width:100px;height:30px;font-size:12px">Read More</div>
  <svg class="edge" style="top:526px" viewBox="0 0 1200 30" preserveAspectRatio="none"><path d="M0 0 L1200 0 L1200 10 L1100 18 L1000 8 L890 20 L780 9 L690 17 L580 7 L470 19 L370 9 L270 18 L160 8 L70 17 L0 9Z" fill="#fff"/></svg>
</section>

<section class="products" role="img" aria-label="Background photo of dark roasted coffee beans">
  <div class="section-title" style="top:100px"><span class="rule"></span>Coffee Product<span class="rule"></span></div>
  <div class="card" style="left:140px"><div class="pack" role="img" aria-label="Black and red coffee bag"></div><h3>Corsa Rosso</h3><div class="wt">1kg Beans</div><div class="price">$ 30.00</div><div class="btn">Add to Cart</div></div>
  <div class="card" style="left:520px"><div class="pack" role="img" aria-label="Black coffee bag"></div><h3>Corsa Nero</h3><div class="wt">1kg Beans</div><div class="price">$ 30.00</div><div class="btn">Add to Cart</div></div>
  <div class="card" style="left:800px"><div class="pack light" role="img" aria-label="Cream and gold coffee bag"></div><h3>Corsa Grande</h3><div class="wt">1kg Beans</div><div class="price">$30.00</div><div class="btn">Add to Cart</div></div>
  <div class="btn" style="left:516px;top:640px;width:168px;height:44px;font-size:13px">View All Products</div>
</section>

<section class="testimonials" role="img" aria-label="Soft background photo of a coffee bag and cup">
  <div class="section-title" style="top:40px"><span class="rule"></span>Testimonials<span class="rule"></span></div>
  <div class="quote-box">
    <h4>Marla Venn</h4>
    <div class="role">Customer</div>
    <p>The beans arrive fresh every single time and the flavour is rich and smooth. Ordering is easy, delivery is quick and the team is always happy to help me pick the right blend for my cafe. I would not buy my coffee anywhere else now.</p>
    <svg style="margin-top:30px" width="36" height="30" viewBox="0 0 36 30"><path d="M2 28V16C2 8 6 3 14 1v5c-4 2-6 5-6 9h6v13ZM22 28V16c0-8 4-13 12-15v5c-4 2-6 5-6 9h6v13Z" fill="#fff"/></svg>
  </div>
  <div class="arrow" style="left:80px"><svg width="14" height="14" viewBox="0 0 14 14"><path d="M9 2 4 7l5 5" stroke="#1e1916" stroke-width="2" fill="none"/></svg></div>
  <div class="arrow" style="left:1080px"><svg width="14" height="14" viewBox="0 0 14 14"><path d="M5 2l5 5-5 5" stroke="#1e1916" stroke-width="2" fill="none"/></svg></div>
</section>

<section class="partners" aria-label="Partner badges">
  <i></i><i></i><i></i><i></i><i></i><i></i>
</section>

<footer class="footer">
  <div class="vip">
    <h3>Join Our VIP Club</h3>
    <div class="field">Your Email Address</div>
    <div class="btn">Subscribe</div>
    <div class="social" style="left:826px"></div>
    <div class="social" style="left:872px"></div>
  </div>
  <div class="foot-brand"><div class="mark">VELCOR<br>&amp; SONS</div></div>
  <p class="foot-text">Trusted importers and exporters of fine coffee and quality goods. Sourced with care, delivered on time and always backed by friendly service.</p>
  <div class="col-title" style="left:560px">Quick Links</div>
  <ul class="links"><li>Home</li><li>Products</li><li>Chamber We Support</li><li>VIP Club</li><li>Contact Us</li></ul>
  <div class="col-title" style="left:784px">Contact Us</div>
  <div class="contact" style="top:228px"><svg width="16" height="16" viewBox="0 0 16 16"><path d="M3 1h3l1 4-2 1a9 9 0 0 0 5 5l1-2 4 1v3c0 1-1 2-2 2C7 15 1 9 1 3c0-1 1-2 2-2Z" fill="#fff"/></svg><span>Call Us: 1300 555 018</span></div>
  <div class="contact" style="top:274px"><svg width="16" height="14" viewBox="0 0 16 14"><rect x="1" y="1" width="14" height="12" fill="none" stroke="#fff" stroke-width="1.5"/><path d="M1 2l7 6 7-6" stroke="#fff" stroke-width="1.5" fill="none"/></svg><span>enquiries@velcorandsons.com.au</span></div>
  <div class="contact" style="top:320px"><svg width="14" height="18" viewBox="0 0 14 18"><path d="M7 1a6 6 0 0 1 6 6c0 4-6 10-6 10S1 11 1 7a6 6 0 0 1 6-6Z" fill="#fff"/><circle cx="7" cy="7" r="2.2" fill="#2b231e"/></svg><span>Address: 12 Harbour Street<br>Sydney NSW 2000 Australia</span></div>
</footer>
<div class="bottom-bar"><span>© Copyright Velcor &amp; Sons 2024</span><span>Terms &amp; Conditions | Privacy Policy</span></div>

</body>
</html>
```